Diesel injection diagnostics and repairs

I am after a business card design for my business.
The business; repairs diesel fuel systems on 4wds, trucks, earthmoving equipment,can do mobile repairs and diagnostics
The business design can basic but effective, I guess some colours such as green and black or even blue......
The end result should reflect the business name and logo and what the business can do

Industry/Entity Type

Business

Contact Information for Business Card

BW Diesel Injection PTY LTD
bw_diesel@trovamail.net
Dennis Holt
0491570156

```html
<!DOCTYPE html>
<html lang="en">
<head>
<meta charset="utf-8">
<title>BW Diesel Injection – Business Card</title>
<link rel="stylesheet" href="https://fonts.googleapis.com/css2?family=Michroma&display=swap">
<style>
  :root {
    --page-bg: #d8d3ca;
    --card-white: #ffffff;
    --card-black: #050505;
    --ink-dark: #111111;
    --ink-light: #f2f2f2;
    --accent-navy: #232a6e;
    --accent-steel: #b9bcc2;
    --shadow: rgba(0, 0, 0, 0.28);
  }
  * { box-sizing: border-box; margin: 0; padding: 0; }
  html, body {
    width: 1200px;
    height: 1000px;
    overflow: hidden;
    background: var(--page-bg);
    font-family: "Michroma", sans-serif;
  }
  .sheet {
    position: relative;
    width: 1200px;
    height: 1000px;
  }
  .card {
    position: absolute;
    left: 250px;
    width: 700px;
    height: 400px;
    box-shadow: 0 12px 30px var(--shadow);
    overflow: hidden;
  }
  /* ---------- Front ---------- */
  .card--front {
    top: 70px;
    background: var(--card-white);
    color: var(--ink-dark);
  }
  .front__band {
    position: absolute;
    top: 0;
    right: 0;
    width: 56px;
    height: 100%;
    background: var(--card-black);
    display: flex;
    align-items: center;
    justify-content: center;
  }
  .front__band-text {
    writing-mode: vertical-rl;
    color: var(--ink-light);
    font-size: 16px;
    letter-spacing: 1px;
    text-transform: uppercase;
    white-space: nowrap;
  }
  .brand {
    display: flex;
    align-items: center;
    gap: 16px;
    text-transform: uppercase;
  }
  .brand__dot {
    width: 44px;
    height: 44px;
    border-radius: 50%;
    background: var(--accent-navy);
    flex: none;
  }
  .front__brand {
    position: absolute;
    top: 70px;
    left: 60px;
    font-size: 26px;
    color: var(--ink-dark);
  }
  .front__contact {
    position: absolute;
    left: 60px;
    bottom: 56px;
    list-style: none;
    font-size: 21px;
    line-height: 1.55;
  }
  .front__name { text-transform: uppercase; font-size: 19px; margin-bottom: 18px; }
  .front__phone { font-size: 25px; }
  /* ---------- Back ---------- */
  .card--back {
    top: 530px;
    background: var(--card-black);
    color: var(--ink-light);
  }
  .back__brand {
    position: absolute;
    top: 150px;
    left: 0;
    width: 100%;
    justify-content: center;
    font-size: 30px;
    color: var(--ink-light);
  }
  .back__rule {
    position: absolute;
    left: 110px;
    right: 110px;
    top: 232px;
    height: 2px;
    background: var(--accent-steel);
  }
  .back__services {
    position: absolute;
    left: 0;
    bottom: 40px;
    width: 100%;
    text-align: center;
    font-size: 13px;
    letter-spacing: 0.5px;
    text-transform: uppercase;
  }
</style>
</head>
<body>
<main class="sheet">
  <section class="card card--front" aria-label="Business card front">
    <div class="front__band">
      <span class="front__band-text">BW Diesel Injection Pty Ltd</span>
    </div>
    <div class="brand front__brand">
      <span class="brand__dot"></span>
      <span class="brand__name">BW Diesel Injection</span>
    </div>
    <ul class="front__contact">
      <li class="front__name">Dennis Holt</li>
      <li class="front__phone">0491570156</li>
      <li class="front__email">bw_diesel@trovamail.net</li>
    </ul>
  </section>

  <section class="card card--back" aria-label="Business card back">
    <div class="brand back__brand">
      <span class="brand__dot"></span>
      <span class="brand__name">BW Diesel Injection</span>
    </div>
    <div class="back__rule"></div>
    <p class="back__services">Common Rail Diagnostics | Fuel System Repairs | Mobile Repairs</p>
  </section>
</main>
</body>
</html>
```